Event Poster for Bar Sunday Live Music and Happy Hour

We are a bar. Every Sunday we have a HARBOUR HOURS event where we have live music and a Sunday Happy Hour. I would like a poster that promotes this weekly event in A4 and A3. Information the poster should include:Event Name: SUNDAY SESSIONSVenue: Copper Lantern 218-222 Marlow Rd PrestonDrink Specials: 3:00 pm - 5:00pmLive Music: 4:30pm -6:30pmAttached is our logo.

Target Market(s)

Both sexes 30-40 year olds

Industry/Entity Type

Hospitality

Font styles to use
Sans Serif

Colors

Designer to choose colors to be used in the design.

Requirements
Must have
• Event Name: HARBOUR HOURS
• Venue: Copper Lantern 218-222 Marlow Rd Preston
• Drink Specials: 3:00 pm - 5:00pm
• Live Music: 4:30pm -6:30pm
• Logo
Nice to have
• Open to different styles and ideas. Like colour.
Should not have
• It should not be too blokey are over the top bar-like.

```html
<!DOCTYPE html>
<html lang="en">
<head>
<meta charset="utf-8">
<title>Harbour Hours Poster</title>
<link rel="stylesheet" href="https://fonts.googleapis.com/css2?family=Exo+2:ital,wght@1,900&family=Nunito:wght@800&family=Oswald:wght@500&display=swap">
<style>
  :root {
    --backdrop: #e6e3de;
    --poster-black: #050505;
    --ink-white: #f4f4f4;
    --accent-orange: #f58220;
    --accent-cyan: #1fb3e6;
    --ribbon-blue: #5bc3e0;
    --ribbon-shade: #2a8aa8;
    --address-yellow: #f6c614;
    --ring-white: #e8e8e8;
  }
  * { margin: 0; padding: 0; box-sizing: border-box; }
  html, body { width: 1200px; height: 1200px; overflow: hidden; background: var(--backdrop); }
  .poster {
    position: absolute; left: 270px; top: 30px;
    width: 660px; height: 1140px;
    background: var(--poster-black);
    overflow: hidden;
  }
  .hero-photo {
    position: absolute; left: 0; top: 0; width: 660px; height: 800px;
    background:
      radial-gradient(ellipse 150px 280px at 330px 470px, rgba(226,130,40,.85), rgba(170,80,20,.4) 60%, transparent 100%),
      radial-gradient(ellipse 160px 300px at 500px 500px, rgba(240,160,60,.85), rgba(180,95,30,.4) 60%, transparent 100%),
      radial-gradient(ellipse 260px 320px at 520px 360px, rgba(110,55,30,.7), transparent 75%),
      linear-gradient(180deg, #050505 0%, #1a0f0a 45%, #2a1a10 75%, #050505 100%);
  }
  .brand {
    position: absolute; top: 120px; left: 0; width: 660px;
    display: flex; justify-content: center; align-items: center; gap: 10px;
    padding-left: 90px;
    font-family: "Oswald", sans-serif; font-weight: 500;
    font-size: 22px; letter-spacing: 3px; color: var(--ring-white);
  }
  .brand-dot { width: 12px; height: 12px; border-radius: 50%; background: var(--ring-white); }
  .time-badge {
    position: absolute; width: 184px; height: 184px; left: 88px;
    display: flex; flex-direction: column; justify-content: center; align-items: center;
    font-family: "Nunito", sans-serif; font-weight: 800; line-height: 1.28;
    text-align: center;
  }
  .time-badge svg { position: absolute; inset: 0; }
  .time-badge .label { color: var(--accent-cyan); font-size: 24px; }
  .time-badge .hours { color: var(--ring-white); font-size: 23px; }
  .time-badge .hours b { color: var(--accent-orange); font-weight: 800; }
  .badge-drinks { top: 210px; }
  .badge-music { top: 485px; }
  .event-title {
    position: absolute; left: 0; width: 660px; text-align: center;
    font-family: "Exo 2", sans-serif; font-weight: 900; font-style: italic;
    text-transform: uppercase; line-height: 1;
  }
  .title-main { top: 735px; font-size: 92px; color: var(--ink-white); -webkit-text-stroke: 2px #111; text-shadow: 3px 3px 0 #555; letter-spacing: 2px; }
  .title-sub { top: 845px; font-size: 80px; color: var(--accent-orange); text-shadow: 3px 3px 0 #4a2000; letter-spacing: 3px; }
  .ribbon { position: absolute; left: 70px; top: 945px; width: 520px; height: 64px; }
  .ribbon-text {
    position: absolute; left: 70px; top: 955px; width: 520px; text-align: center;
    font-family: "Oswald", sans-serif; font-weight: 500; font-size: 24px;
    color: var(--ink-white); letter-spacing: .5px; transform: rotate(-2deg);
  }
  .venue-line {
    position: absolute; left: 0; top: 1028px; width: 660px; text-align: center;
    font-family: "Oswald", sans-serif; font-weight: 500; font-size: 27px;
    color: var(--address-yellow); transform: rotate(-2deg);
  }
</style>
</head>
<body>
  <main class="poster">
    <div class="hero-photo" role="img" aria-label="Two tulip glasses of amber beer on a wooden bar table in a dim pub"></div>

    <div class="brand"><span class="brand-dot"></span>COPPER LANTERN</div>

    <div class="time-badge badge-drinks">
      <svg width="184" height="184" viewBox="0 0 184 184"><circle cx="92" cy="92" r="86" fill="none" stroke="var(--ring-white)" stroke-width="3"/><circle cx="93" cy="91" r="80" fill="none" stroke="var(--ring-white)" stroke-width="1.5" opacity=".7"/></svg>
      <span class="label">Drink<br>Specials:</span>
      <span class="hours"><b>3:00</b> pm To<br><b>5:00</b> pm</span>
    </div>

    <div class="time-badge badge-music">
      <svg width="184" height="184" viewBox="0 0 184 184"><circle cx="92" cy="92" r="86" fill="none" stroke="var(--ring-white)" stroke-width="3"/><circle cx="93" cy="91" r="80" fill="none" stroke="var(--ring-white)" stroke-width="1.5" opacity=".7"/></svg>
      <span class="label">Live<br>Music:</span>
      <span class="hours"><b>4:30</b> pm To<br><b>6:30</b> pm</span>
    </div>

    <h1 class="event-title title-main">Harbour</h1>
    <h2 class="event-title title-sub">Hours</h2>

    <svg class="ribbon" viewBox="0 0 520 64">
      <polygon points="0,34 40,30 40,62 20,58 6,62" fill="var(--ribbon-shade)"/>
      <polygon points="520,16 480,14 480,46 500,46 514,48" fill="var(--ribbon-shade)"/>
      <polygon points="22,20 498,4 498,40 22,56" fill="var(--ribbon-blue)"/>
    </svg>
    <p class="ribbon-text">LIVE MUSIC AND A SUNDAY HAPPY HOUR</p>

    <p class="venue-line">COPPER LANTERN 218-222 MARLOW RD PRESTON</p>
  </main>
</body>
</html>
```